New Website for NY and South Florida Based Accounting Firm

Accounting and Audit firm located in New York and South Florida needs a website redesign after acquiring new businesses and adding new services.

Our current website can be found here:
http://www.trqbnllp.example/

We have merged with this firm:
http://hollisbarkerwendtfield.example/

We are looking for a comprehensive design that will highlight the firm's dual locations. The final design should communicate security, strength, and growth. We would like to keep our pyramid logo as seen on the trqbnllp.example website, as this has been our logo for over 20 years.

Industry/Entity Type

Accounting

Number of Pages Required

1 page

Font styles to use
Serif
Sans Serif

```html
<!DOCTYPE html>
<html lang="en">
<head>
<meta charset="utf-8">
<title>Thornbury, Quill, Brandt &amp; Nolan, LLP</title>
<link href="https://fonts.googleapis.com/css2?family=Lato:ital,wght@0,300;0,400;0,700;1,400&family=Cabin:wght@600&family=Playball&display=swap" rel="stylesheet">
<style>
:root{
  --gold:#e8a90a;
  --navy:#1b3048;
  --navy-deep:#162a40;
  --ink:#1e2f42;
  --text:#333;
  --line:#d8d8d8;
  --white:#fff;
}
*{margin:0;padding:0;box-sizing:border-box}
html,body{width:1191px;height:1200px;overflow:hidden}
body{position:relative;font-family:Lato,sans-serif;color:var(--text);background:#fff;font-size:13px}
.topline{position:absolute;top:0;left:0;width:1191px;height:4px;background:var(--gold)}
.brand{position:absolute;left:142px;top:20px;display:flex;align-items:center;gap:14px}
.brand-mark{width:110px;height:60px;background:var(--gold)}
.brand-name{font-family:Cabin,sans-serif;font-weight:600;font-size:23px;line-height:29px;color:#333;letter-spacing:.3px}
.phone-tab{position:absolute;left:868px;top:0;width:190px;height:33px;background:var(--gold);border-radius:0 0 22px 22px;color:#fff;font-weight:700;font-size:17px;display:flex;align-items:center;justify-content:center;gap:6px}
.login{position:absolute;left:886px;top:50px;width:142px;height:34px;background:#2a2a2a;border-radius:3px;color:#fff;font-size:13px;display:flex;align-items:center;justify-content:center;gap:7px}
.nav{position:absolute;top:98px;left:0;width:1191px;height:46px;background:var(--navy)}
.nav ul{list-style:none;display:flex;position:absolute;left:130px;top:0;height:46px}
.nav li{color:#fff;font-weight:700;font-size:13.5px;letter-spacing:.3px;padding:0 24px;line-height:46px;border-right:1px solid #2e4862;position:relative}
.nav li:last-child{border-right:none;padding-right:0}
.nav li.active::after{content:"";position:absolute;left:18px;right:24px;bottom:9px;height:2px;background:var(--gold)}
.nav li.active{padding-left:18px}
.hero{position:absolute;top:144px;left:0;width:1191px;height:459px;background:linear-gradient(160deg,#b7b2ac 0%,#8b8782 40%,#6a6d72 70%,#3e4c5e 100%)}
.hero-shade{position:absolute;inset:0;background:rgba(20,25,32,.35)}
.hero h1{position:absolute;left:0;width:1191px;top:170px;text-align:center;font-family:Playball,cursive;font-weight:400;color:#fff;font-size:42px;line-height:62px;text-shadow:0 2px 6px rgba(0,0,0,.5)}
.arrow{position:absolute;top:209px;width:52px;height:49px;background:#ccc;padding:4px}
.arrow span{display:flex;align-items:center;justify-content:center;width:100%;height:100%;background:#333}
.arrow.prev{left:14px}.arrow.next{right:0}
.content{position:absolute;left:129px;top:568px;width:931px;height:333px;background:#fff;box-shadow:0 0 12px rgba(0,0,0,.12)}
.col{position:absolute;top:18px;width:260px}
.col + .col{}
.col.about{left:26px}.col.services{left:336px}.col.inquiry{left:647px;width:263px}
.divider{position:absolute;top:24px;width:1px;height:290px;background:#eee}
.col h2{font-weight:400;font-size:25px;color:var(--ink);border-bottom:1px solid var(--line);padding-bottom:2px;position:relative}
.col h2 em{font-style:normal;color:var(--gold)}
.col h2::after{content:"";position:absolute;left:0;bottom:-1px;width:82px;height:2px;background:var(--ink)}
.photo{margin-top:16px;width:260px;height:132px;background:linear-gradient(120deg,#a9c6e2,#e6eef5 60%,#9fb1c2)}
.about p{margin-top:10px;font-size:14px;line-height:21px;color:#444;padding-left:2px}
.btn{position:absolute;top:284px;width:90px;height:25px;border:2px solid #333;border-radius:13px;background:var(--gold);color:#222;font-size:12px;display:flex;align-items:center;justify-content:center}
.services ul{list-style:none;margin-top:14px}
.services li{position:relative;padding-left:22px;font-size:13.5px;line-height:18px;color:var(--ink);margin-bottom:6px}
.services li svg{position:absolute;left:0;top:2px}
.field{margin-top:16px;width:263px;height:39px;border:1px solid #bbb;font-style:italic;color:#444;font-size:14.5px;padding:10px 9px}
.field + .field{margin-top:14px}
.field.msg{height:94px}
.footer{position:absolute;top:901px;left:0;width:1191px;height:263px;background:var(--navy-deep)}
.fcol{position:absolute;top:18px;color:#e8ecf0}
.fcol h3{font-weight:300;font-size:21px;color:#fff;border-bottom:1px solid #6f7f90;padding-bottom:6px}
.quick{left:140px;width:125px}
.quick ul{list-style:none;margin-top:6px}
.quick li{font-size:13.5px;line-height:24.7px;padding-left:15px;position:relative}
.quick li::before{content:"›";position:absolute;left:0;color:#aaa}
.member{left:331px;width:277px}
.member ul{list-style:none;margin-top:6px}
.member li{font-size:13.5px;line-height:26px}
.vrule{position:absolute;top:56px;width:1px;height:190px;background:#24394f}
.contact{left:675px;width:385px}
.office{position:absolute;left:0;font-size:13.5px;line-height:17px}
.office strong{display:block;font-weight:400;font-size:14.5px;margin-bottom:6px;padding-left:26px}
.office span{display:block;padding-left:26px}
.office svg{position:absolute;left:0;top:1px}
.cline{position:absolute;left:252px;font-size:13.5px;display:flex;gap:12px;align-items:center}
.social{position:absolute;left:253px;top:200px;display:flex;gap:14px}
.social i{width:22px;height:22px;background:#fff;display:block}
.bottombar{position:absolute;top:1164px;left:0;width:1191px;height:36px;background:var(--gold);color:#2a2a2a;font-size:13.5px;text-align:center;line-height:36px}
</style>
</head>
<body>
<div class="topline"></div>
<header>
  <div class="brand">
    <div class="brand-mark"></div>
    <div class="brand-name">THORNBURY, QUILL,<br>BRANDT &amp; NOLAN, LLP</div>
  </div>
  <div class="phone-tab">
    <svg width="15" height="15" viewBox="0 0 24 24"><path fill="#fff" d="M6.6 10.8a15 15 0 0 0 6.6 6.6l2.2-2.2c.3-.3.7-.4 1-.2 1.1.4 2.3.6 3.6.6.6 0 1 .4 1 1V20c0 .6-.4 1-1 1A17 17 0 0 1 3 4c0-.6.4-1 1-1h3.5c.6 0 1 .4 1 1 0 1.3.2 2.5.6 3.6.1.3 0 .7-.2 1z"/></svg>
    555-014-7890
  </div>
  <div class="login">
    <svg width="11" height="13" viewBox="0 0 11 13"><rect x="0" y="5.5" width="11" height="7.5" fill="#fff"/><path d="M2.5 5.5V3.5a3 3 0 0 1 6 0v2" stroke="#fff" stroke-width="1.6" fill="none"/></svg>
    CLIENT LOGIN
  </div>
</header>
<nav class="nav">
  <ul>
    <li class="active">HOME</li><li>WHY TRQBN?</li><li>SERVICES</li><li>PROFILES</li><li>TIPS &amp; LINKS</li><li>PARTNERS</li><li>RESOURCES</li><li>CONTACT US</li>
  </ul>
</nav>
<section class="hero" role="img" aria-label="Close-up of hands reviewing a printed financial bar chart with a pen">
  <div class="hero-shade"></div>
  <h1>TRQBN Is A Tax, Audit And Business Advisory Practice<br>With Over 30 Professionals In NYC And Long Island.</h1>
  <div class="arrow prev"><span><svg width="12" height="16" viewBox="0 0 12 16"><path d="M9 2L3 8l6 6" stroke="#fff" stroke-width="3" fill="none"/></svg></span></div>
  <div class="arrow next"><span><svg width="12" height="16" viewBox="0 0 12 16"><path d="M3 2l6 6-6 6" stroke="#fff" stroke-width="3" fill="none"/></svg></span></div>
</section>
<main class="content">
  <div class="col about">
    <h2>ABOUT <em>TRQBN</em></h2>
    <div class="photo" role="img" aria-label="Smiling senior businessman in shirt and tie with colleagues in an office behind"></div>
    <p>Lorem ipsum dolor sit amet, consectetuer adipiscing elit, sed diam nonummy nibh euismod magna aliquam erat volutpat.</p>
  </div>
  <div class="btn" style="left:40px">Read More</div>
  <div class="divider" style="left:308px"></div>
  <div class="col services">
    <h2>OUR <em>SERVICES</em></h2>
    <ul>
      <li><svg width="14" height="12" viewBox="0 0 14 12"><path d="M1 6l4 4 8-9" stroke="#e8a90a" stroke-width="2.2" fill="none"/></svg>Condominium, Homeowner &amp; Timeshare Association Services/Auditor</li>
      <li><svg width="14" height="12" viewBox="0 0 14 12"><path d="M1 6l4 4 8-9" stroke="#e8a90a" stroke-width="2.2" fill="none"/></svg>Audit, Review, and Attestation Services</li>
      <li><svg width="14" height="12" viewBox="0 0 14 12"><path d="M1 6l4 4 8-9" stroke="#e8a90a" stroke-width="2.2" fill="none"/></svg>Accounting And Tax Services</li>
      <li><svg width="14" height="12" viewBox="0 0 14 12"><path d="M1 6l4 4 8-9" stroke="#e8a90a" stroke-width="2.2" fill="none"/></svg>Non Profit Audits/Auditors</li>
      <li><svg width="14" height="12" viewBox="0 0 14 12"><path d="M1 6l4 4 8-9" stroke="#e8a90a" stroke-width="2.2" fill="none"/></svg>Grant Audits/Auditors</li>
      <li><svg width="14" height="12" viewBox="0 0 14 12"><path d="M1 6l4 4 8-9" stroke="#e8a90a" stroke-width="2.2" fill="none"/></svg>Single And OMB 133 Audits/Auditors</li>
      <li><svg width="14" height="12" viewBox="0 0 14 12"><path d="M1 6l4 4 8-9" stroke="#e8a90a" stroke-width="2.2" fill="none"/></svg>401-K Audits/Auditors</li>
      <li><svg width="14" height="12" viewBox="0 0 14 12"><path d="M1 6l4 4 8-9" stroke="#e8a90a" stroke-width="2.2" fill="none"/></svg>Bookkeeping (Compliance Services)</li>
    </ul>
  </div>
  <div class="btn" style="left:336px">Read More</div>
  <div class="divider" style="left:625px"></div>
  <div class="col inquiry">
    <h2>QUICK <em>INQUIRY</em></h2>
    <div class="field">Name</div>
    <div class="field">Email</div>
    <div class="field msg">Message</div>
  </div>
  <div class="btn" style="left:647px">Submit</div>
</main>
<footer class="footer">
  <div class="fcol quick">
    <h3>Quick Links</h3>
    <ul><li>Home</li><li>Why Trqbn?</li><li>Services</li><li>Profiles</li><li>Tips &amp; Links</li><li>Partners</li><li>Resources</li><li>Contact</li></ul>
  </div>
  <div class="vrule" style="left:293px"></div>
  <div class="fcol member">
    <h3>Member</h3>
    <ul><li>LedgerCircle Network</li><li>National Guild of Accountants</li><li>Empire State Accountants Council</li><li>Guild Personal Financial Planning Division</li></ul>
  </div>
  <div class="vrule" style="left:636px"></div>
  <div class="fcol contact">
    <h3>Contact Details</h3>
    <div class="office" style="top:50px"><svg width="12" height="16" viewBox="0 0 12 16"><path d="M6 0a6 6 0 0 0-6 6c0 4.5 6 10 6 10s6-5.5 6-10a6 6 0 0 0-6-6zm0 8.5A2.5 2.5 0 1 1 6 3.5a2.5 2.5 0 0 1 0 5z" fill="#fff"/></svg><strong>New York Office</strong><span>1200 Meridian Plaza</span><span>2nd Floor New York, NY 10001</span></div>
    <div class="office" style="top:117px"><svg width="12" height="16" viewBox="0 0 12 16"><path d="M6 0a6 6 0 0 0-6 6c0 4.5 6 10 6 10s6-5.5 6-10a6 6 0 0 0-6-6zm0 8.5A2.5 2.5 0 1 1 6 3.5a2.5 2.5 0 0 1 0 5z" fill="#fff"/></svg><strong>Long Island Office</strong><span>48 Harbor Crest Road</span><span>Melville, NY 11700</span></div>
    <div class="office" style="top:185px"><svg width="12" height="16" viewBox="0 0 12 16"><path d="M6 0a6 6 0 0 0-6 6c0 4.5 6 10 6 10s6-5.5 6-10a6 6 0 0 0-6-6zm0 8.5A2.5 2.5 0 1 1 6 3.5a2.5 2.5 0 0 1 0 5z" fill="#fff"/></svg><strong>Florida Office</strong><span>750 NW Palm Street, Suite 110</span><span>Fort Lauderdale, FL 33300</span></div>
    <div class="cline" style="top:52px"><svg width="14" height="14" viewBox="0 0 24 24"><path fill="#fff" d="M6.6 10.8a15 15 0 0 0 6.6 6.6l2.2-2.2c.3-.3.7-.4 1-.2 1.1.4 2.3.6 3.6.6.6 0 1 .4 1 1V20c0 .6-.4 1-1 1A17 17 0 0 1 3 4c0-.6.4-1 1-1h3.5c.6 0 1 .4 1 1 0 1.3.2 2.5.6 3.6.1.3 0 .7-.2 1z"/></svg>555-201-4480</div>
    <div class="cline" style="top:81px"><svg width="14" height="14" viewBox="0 0 24 24"><path fill="#fff" d="M6.6 10.8a15 15 0 0 0 6.6 6.6l2.2-2.2c.3-.3.7-.4 1-.2 1.1.4 2.3.6 3.6.6.6 0 1 .4 1 1V20c0 .6-.4 1-1 1A17 17 0 0 1 3 4c0-.6.4-1 1-1h3.5c.6 0 1 .4 1 1 0 1.3.2 2.5.6 3.6.1.3 0 .7-.2 1z"/></svg>(555) 386-1995</div>
    <div class="cline" style="top:111px"><svg width="14" height="13" viewBox="0 0 14 13"><rect x="3" y="0" width="8" height="4" fill="#fff"/><rect x="0" y="4" width="14" height="6" rx="1" fill="#fff"/><rect x="3" y="8" width="8" height="5" fill="#fff" stroke="#162a40"/></svg>555-201-4493</div>
    <div class="cline" style="top:141px"><svg width="14" height="13" viewBox="0 0 14 13"><rect x="3" y="0" width="8" height="4" fill="#fff"/><rect x="0" y="4" width="14" height="6" rx="1" fill="#fff"/><rect x="3" y="8" width="8" height="5" fill="#fff" stroke="#162a40"/></svg>(555) 386-2399</div>
    <div class="cline" style="top:171px"><svg width="15" height="11" viewBox="0 0 15 11"><rect x="0" y="0" width="15" height="11" fill="#fff"/><path d="M0 0l7.5 6L15 0" stroke="#162a40" fill="none"/></svg>info@trqbnllp.example</div>
    <div class="social"><i></i><i></i><i></i><i></i></div>
  </div>
</footer>
<div class="bottombar">© 2016 Thornbury, Quill, Brandt &amp; Nolan, Llp &nbsp;|&nbsp; All Rights Reserved</div>
</body>
</html>
```